依頼詳細
オープン記念として駅前や近隣住宅に初回割引きチケット付きのチラシを配ろうと思います。そのチラシデザインをお願い致します。思わず撮りたくなるような、オシャレなデザインをお願い致します。チケットは初回撮影代3,000円(税込3,300円)のチケットでお願いします。
記載項目
店舗名:studio Lantern 川越店
住所:350-0871 埼玉県川越市松葉台3-8-5コハクビル2F
最寄駅:北桜台駅徒歩1分、東峰原駅徒歩6分、朝霧坂駅徒歩12分
電話番号:049-318-6924
営業時間:10時00分~18時00分
URL:https://studio-lantern-foto.com
Instagram:@studiolantern_kawagoe
LINE:QRコード別途添付
ロゴ:別途添付png
キャッチコピー:誰もが持つ、誰にも見せない美しさを形に。
メニュー:マタニティ、ニューボーン(お宮参り)、バースデー、七五三、家族写真、ロケーション撮影
料金: 撮影、衣装、着付け、ヘアメイクすべて込みで 初回撮影料3,000円(税込3,300円) + 商品代
商品例:撮影データ、アルバム、木製パネル、等身大パネル、フレーム、スマホケース等
予約方法:HP予約、公式LINE、またはInstagramのDMにて予約可能
サイズ
A4
ページ数
片面
希望イメージ
シンプル 複雑
単色 カラフル
暗い 明るい
日常 高級
遊び心 厳粛
未来的 伝統的
女性的 男性的
希望する色
納品ファイル
• イラストレーター形式 (.ai)
補足説明
LINEQRコード、
スタジオのロゴ、
スタジオ写真3枚などを添付しますが
全て使用しなくても構いません。
また足りない等あればご相談ください。
LINEデータとロゴデータが見れなかったようなので再度アップロードさせていただきます。

オシャレさ、店舗イメージが明確に表現できており
社内で満場一致で決まりました。

提案していただき皆様ありがとうございました。
またの機会には宜しくお願い致します。

```html
<!DOCTYPE html>
<html lang="ja">
<head>
<meta charset="UTF-8">
<title>studio Lantern 川越店 NEW OPEN</title>
<link rel="stylesheet" href="https://fonts.googleapis.com/css2?family=Cormorant+Garamond:wght@400;500&family=Noto+Serif+JP:wght@400;500;700&family=Noto+Sans+JP:wght@400;500;700&display=swap">
<style>
:root{
  --ink:#0c0c0c;
  --white:#ffffff;
  --pink:#d98298;
  --pink-pale:#f7e4ea;
  --text:#2a2a2a;
  --grey:#8a8a8a;
  --gold:#c9a45a;
}
*{margin:0;padding:0;box-sizing:border-box}
html,body{width:849px;height:1200px;overflow:hidden;background:var(--white)}
.flyer{position:relative;width:849px;height:1200px;overflow:hidden;font-family:"Noto Sans JP",sans-serif;color:var(--text)}
.hero{position:absolute;left:0;top:0;width:849px;height:880px;background:var(--ink)}
.hero__photo{position:absolute;left:300px;top:180px;width:549px;height:700px;
  background:radial-gradient(ellipse at 55% 45%,#9a9a9a 0%,#555 35%,#1c1c1c 70%,var(--ink) 100%)}
.hero__frames{position:absolute;left:0;top:0}
.catch{position:absolute;left:205px;top:24px;writing-mode:vertical-rl;font-family:"Noto Serif JP",serif;
  font-size:18px;line-height:36px;letter-spacing:.18em;color:var(--white)}
.brand{position:absolute;left:42px;top:412px;display:flex;align-items:center;gap:10px;color:var(--white);
  font-family:"Noto Serif JP",serif;font-size:22px}
.brand__mark{width:22px;height:22px;background:var(--white)}
.headline{position:absolute;left:40px;top:462px;font-family:"Cormorant Garamond",serif;font-weight:400;
  font-size:70px;line-height:66px;color:var(--white);letter-spacing:.02em}
.subline{position:absolute;left:42px;top:612px;font-family:"Cormorant Garamond",serif;font-size:17px;color:var(--white);letter-spacing:.04em}
.features{position:absolute;left:42px;top:652px;display:grid;grid-template-columns:116px 116px;gap:8px;list-style:none}
.features li{height:30px;border:1px solid var(--white);color:var(--white);font-family:"Noto Serif JP",serif;
  font-size:12px;display:flex;align-items:center;justify-content:center;letter-spacing:.1em}
.menu{position:absolute;left:0;top:888px;width:849px;text-align:center;font-family:"Noto Serif JP",serif;
  font-size:14px;color:var(--pink);letter-spacing:.08em;word-spacing:.6em}
.ticket{position:absolute;left:40px;top:916px;width:560px;height:96px;border:1.5px solid var(--pink);display:flex;align-items:center;padding:0 14px;gap:14px}
.ticket__label{width:56px;height:56px;background:var(--pink);color:var(--white);font-size:12px;font-weight:700;
  display:flex;align-items:center;justify-content:center;text-align:center;line-height:1.3}
.ticket__price{font-family:"Noto Serif JP",serif;font-weight:700;font-size:50px;color:var(--pink);line-height:1}
.ticket__tax{font-size:10px;color:var(--pink);align-self:flex-start;margin-top:26px;margin-left:-10px}
.ticket__plus{font-family:"Noto Serif JP",serif;font-weight:700;font-size:28px;color:var(--pink)}
.ticket__note{position:absolute;left:86px;bottom:6px;font-size:11px;color:var(--text)}
.products{position:absolute;left:40px;top:1017px;font-size:9px;color:var(--grey)}
.samples{position:absolute;left:622px;top:914px}
.contact{position:absolute;left:40px;top:1044px;width:770px;height:120px}
.contact__brand{position:absolute;left:0;top:18px;display:flex;flex-direction:column;align-items:center;gap:6px;font-family:"Noto Serif JP",serif;font-size:11px}
.contact__brand .brand__mark{width:28px;height:28px;background:var(--text)}
.contact__name{position:absolute;left:108px;top:0;font-family:"Noto Serif JP",serif;font-size:22px;font-weight:500}
.contact__address{position:absolute;left:108px;top:38px;font-size:9px;line-height:1.6;color:var(--text)}
.contact__tel{position:absolute;left:410px;top:2px;font-family:"Noto Serif JP",serif;font-size:21px;font-weight:500;display:flex;align-items:center;gap:6px}
.contact__info{position:absolute;left:410px;top:38px;font-size:10px;line-height:1.7}
.corner{position:absolute;right:0;bottom:28px}
.reserve{position:absolute;left:0;bottom:0;width:849px;height:28px;background:var(--pink-pale);color:var(--text);
  font-size:12px;display:flex;align-items:center;justify-content:center;letter-spacing:.05em}
</style>
</head>
<body>
<div class="flyer">
  <section class="hero">
    <div class="hero__photo" role="img" aria-label="妊婦の女性が布をまとって座るモノクロのマタニティ写真"></div>
    <svg class="hero__frames" width="849" height="880" viewBox="0 0 849 880" aria-hidden="true">
      <g fill="none" stroke="#ffffff" stroke-width="2">
        <rect x="360" y="250" width="330" height="540" transform="rotate(-7 525 520)"/>
        <rect x="380" y="270" width="300" height="510" transform="rotate(5 530 525)"/>
      </g>
    </svg>
    <p class="catch">誰もが持つ、<br>誰にも見せない美しさを形に。</p>
    <div class="brand"><span class="brand__mark"></span><span>studio Lantern</span></div>
    <h1 class="headline">NEW<br>OPEN</h1>
    <p class="subline">Maternity &amp; Baby Photo Studio</p>
    <ul class="features">
      <li>完全貸切</li><li>衣裳多数</li><li>女性スタッフ</li><li>全データ販売</li>
    </ul>
  </section>

  <p class="menu">マタニティ ニューボーン(お宮参り) バースデー 七五三 家族写真 ロケーション撮影</p>

  <div class="ticket">
    <div class="ticket__label">初回<br>撮影料</div>
    <span class="ticket__price">¥3,000</span>
    <span class="ticket__tax">(税込3,300円)</span>
    <span class="ticket__plus">+商品代</span>
    <p class="ticket__note">撮影、衣装、着付け、ヘアメイク込み</p>
  </div>
  <p class="products">※商品例：撮影データ、アルバム、木製パネル、等身大パネル、フレーム、スマホケース等</p>

  <svg class="samples" width="200" height="100" viewBox="0 0 200 100">
    <g transform="rotate(-6 60 50)"><rect x="10" y="12" width="110" height="78" fill="#ffffff" stroke="#444" stroke-width="2"/>
      <rect x="16" y="18" width="98" height="66" fill="#6d6d6d" role="img" aria-label="ニューボーン撮影のサンプル写真"/></g>
    <g transform="rotate(5 150 50)"><rect x="90" y="16" width="106" height="76" fill="#ffffff" stroke="#444" stroke-width="2"/>
      <rect x="96" y="22" width="94" height="64" fill="#8a8a8a" role="img" aria-label="家族写真のサンプル写真"/></g>
  </svg>

  <div class="contact">
    <div class="contact__brand"><span class="brand__mark"></span><span>studio Lantern</span></div>
    <p class="contact__name">studio Lantern 川越店</p>
    <p class="contact__address">350-0871 埼玉県川越市松葉台3-8-5コハクビル2F<br>北桜台駅 徒歩1分、東峰原駅 徒歩6分、<br>朝霧坂駅 徒歩12分</p>
    <p class="contact__tel">
      <svg width="16" height="16" viewBox="0 0 24 24" aria-hidden="true"><path fill="#2a2a2a" d="M6.6 10.8a15 15 0 0 0 6.6 6.6l2.2-2.2a1 1 0 0 1 1-.25 11.4 11.4 0 0 0 3.6.57 1 1 0 0 1 1 1V20a1 1 0 0 1-1 1A17 17 0 0 1 3 4a1 1 0 0 1 1-1h3.5a1 1 0 0 1 1 1c0 1.25.2 2.45.57 3.57a1 1 0 0 1-.25 1z"/></svg>
      TEL.049-318-6924</p>
    <p class="contact__info">https://studio-lantern-foto.com<br>営業時間 10:00～18:00<br>Instagram @studiolantern_kawagoe</p>
  </div>

  <svg class="corner" width="70" height="70" viewBox="0 0 70 70">
    <polygon points="70,0 70,70 0,70" fill="var(--gold)"/>
    <text x="52" y="60" fill="#ffffff" font-family="Cormorant Garamond, serif" font-size="13" text-anchor="middle" transform="rotate(-45 52 56)">OPEN</text>
  </svg>

  <p class="reserve">ご予約・お問い合わせは、ホームページ、公式LINE、またはInstagramのDMにて</p>
</div>
</body>
</html>
```